Home Page Design

We have a B2B home page design and need a consumer version. The look and feel can look similar but needs to be distinctly different so it in not to get confused. Essentially it should look like the same company with a different model. We will need a PSD w all layers organized and easy to understand. Attached is the logo, B2B comp, and a MS Word doc with a short description. In addition, I have attached a wire frame to be used as a site map. PLEASE DO NOT take that as the creative. I expect to see your creative based on the information provided.

Industry/Entity Type

Consumer

```html
<!DOCTYPE html>
<html lang="en">
<head>
<meta charset="utf-8">
<title>GoodCaddie.com – Home</title>
<link rel="stylesheet" href="https://fonts.googleapis.com/css2?family=Mulish:wght@400;600;700&display=swap">
<style>
:root{
  --green:#3ab54a;
  --green-dark:#2e9a3d;
  --blue:#1f6fae;
  --blue-dark:#175a8e;
  --ink:#222;
  --muted:#555;
  --line:#d9d9d9;
  --track:#f2f2f2;
  --white:#fff;
}
*{box-sizing:border-box;margin:0;padding:0}
html,body{width:1200px;height:2910px;overflow:hidden;background:var(--white)}
body{position:relative;font-family:"Mulish",sans-serif;color:var(--ink)}
.abs{position:absolute}
.top-rule{left:0;top:0;width:1200px;height:8px;background:var(--green)}
.brand{display:flex;align-items:center;gap:18px;color:var(--green);font-weight:600;font-size:32px}
.brand-dot{width:56px;height:56px;border-radius:50%;background:var(--blue)}
.site-brand{left:34px;top:36px}
.account-links{right:22px;top:14px;font-size:17px;color:#888}
.main-nav{top:104px;left:0;width:1200px;font-size:23px;color:var(--blue-dark)}
.main-nav a{position:absolute;color:inherit;text-decoration:none;white-space:nowrap}
.main-nav a.active{color:var(--green);text-decoration:underline}
.hero{left:0;top:146px;width:1200px;height:268px;
  background:linear-gradient(180deg,#b9d6ea 0%,#d7e6ee 18%,#3fb3bf 30%,#2a9fae 38%,#5b7d3b 46%,#3f7a2c 58%,#6c9e3c 75%,#7fae47 100%)}
.hero-arrow{top:230px}
.hero-copy{left:794px;top:228px;width:320px;color:var(--white)}
.hero-copy h2{font-size:22px;font-weight:700;margin-bottom:6px}
.hero-copy p{font-size:14px;line-height:18px}
.btn-join{display:inline-block;margin-top:14px;background:var(--blue);color:var(--white);font-size:15px;padding:5px 8px;border-radius:3px}
.section-title{font-size:27px;color:var(--blue-dark);font-weight:400}
.see-more{font-size:17px;color:var(--green)}
.big-title{left:0;width:1200px;text-align:center;color:var(--green);font-weight:600}
.event-card{width:208px;height:320px;border:2px solid #e2e2e2;border-radius:6px;background:var(--white);overflow:hidden}
.event-card .thumb{height:162px;background:linear-gradient(180deg,#9cc4e0 0%,#7fae56 45%,#4f8f2e 100%)}
.event-card .thumb.t2{background:linear-gradient(180deg,#7fb8e6 0%,#3f7d36 30%,#61a03d 100%)}
.event-card .thumb.t3{background:linear-gradient(180deg,#a9c6dd 0%,#cfc8b5 35%,#4b8a2e 60%,#6aa844 100%)}
.event-card .thumb.t4{background:linear-gradient(180deg,#d6e2ea 0%,#b8cfd9 35%,#6ea246 60%,#4f8c2e 100%)}
.event-card .body{padding:12px 10px 0 10px;font-size:12px;color:var(--ink)}
.event-card h3{font-size:13px;font-weight:700}
.event-card .date{color:var(--muted);margin-top:4px}
.event-card .joined{margin-top:26px;color:var(--muted)}
.progress{margin-top:8px;height:20px;width:188px;border:1px solid #cfcfcf;border-radius:10px;background:var(--track);overflow:hidden}
.progress span{display:block;height:100%;background:var(--green);border-radius:10px}
.event-card .quota{text-align:right;margin-top:10px;color:var(--muted);font-size:11px}
.tile{overflow:hidden}
.tile .label{position:absolute;left:6px;color:var(--white);font-size:19px;font-weight:600;line-height:20px;text-shadow:0 1px 2px rgba(0,0,0,.4)}
.tile.small .label{font-size:14px;line-height:16px}
.cat-list a{position:absolute;font-size:15px;color:var(--blue);text-decoration:none;border-left:3px solid var(--blue);padding-left:6px;line-height:18px;white-space:nowrap}
.cat-list a.active{color:var(--green);border-color:var(--green)}
.field{display:flex;height:48px;border:2px solid var(--green);border-radius:6px;overflow:hidden;font-size:21px}
.field .key{background:var(--green);color:var(--white);padding:0 10px;display:flex;align-items:center}
.field .val{flex:1;color:var(--green);padding:0 14px;display:flex;align-items:center;justify-content:space-between}
.btn-search{background:var(--green);color:var(--white);font-size:21px;border-radius:6px;display:flex;align-items:center;justify-content:center}
.view-more{left:0;width:1200px;text-align:center;font-size:14px;color:#444}
.footer-rule{left:0;top:2784px;width:1200px;height:8px;background:var(--green)}
.footer-rule2{left:0;top:2798px;width:1200px;height:2px;background:var(--green)}
.footer-brand{left:18px;top:2816px;font-size:24px}
.footer-brand .brand-dot{width:44px;height:44px}
</style>
</head>
<body>
<div class="abs top-rule"></div>

<header>
  <div class="abs brand site-brand"><span class="brand-dot"></span><span>GoodCaddie.com</span></div>
  <div class="abs account-links">Sign up | Log in</div>
  <nav class="abs main-nav">
    <a style="left:476px">Start Your Event</a>
    <a class="active" style="left:686px">Explore Auction Items</a>
    <a style="left:960px">About Us</a>
    <a style="left:1098px">Contact</a>
  </nav>
</header>

<section>
  <div class="abs hero" role="img" aria-label="Photo of a seaside golf course with turquoise water, trees and a green fairway"></div>
  <svg class="abs hero-arrow" style="left:12px" width="40" height="90" viewBox="0 0 40 90"><polyline points="32,6 8,45 32,84" fill="none" stroke="rgba(255,255,255,.8)" stroke-width="9"/></svg>
  <svg class="abs hero-arrow" style="left:1148px" width="40" height="90" viewBox="0 0 40 90"><polyline points="8,6 32,45 8,84" fill="none" stroke="rgba(255,255,255,.8)" stroke-width="9"/></svg>
  <div class="abs hero-copy">
    <h2>Seacliff Links</h2>
    <p>Loremipsum dolor sit amet, consectetur adipiscing elit. Phasellus non arcu et risus luctus feugiat.</p>
    <span class="btn-join">Join now</span>
  </div>
</section>

<section>
  <h2 class="abs section-title" style="left:150px;top:446px">Featured Events</h2>
  <div class="abs see-more" style="left:968px;top:460px">See more</div>
  <svg class="abs" style="left:36px;top:598px" width="48" height="96" viewBox="0 0 48 96"><polyline points="38,4 10,48 38,92" fill="none" stroke="var(--blue-dark)" stroke-width="11"/></svg>
  <svg class="abs" style="left:1114px;top:598px" width="48" height="96" viewBox="0 0 48 96"><polyline points="10,4 38,48 10,92" fill="none" stroke="var(--blue-dark)" stroke-width="11"/></svg>

  <article class="abs event-card" style="left:150px;top:502px">
    <div class="thumb" role="img" aria-label="Photo of a parkland golf course with autumn trees"></div>
    <div class="body"><h3>Rivermoor Country Club</h3><div class="date">November 12 , 2014</div><div class="joined">56 people joined</div><div class="progress"><span style="width:82%"></span></div><div class="quota">38 quota left</div></div>
  </article>
  <article class="abs event-card" style="left:380px;top:502px">
    <div class="thumb t2" role="img" aria-label="Photo of a golfer teeing off on a coastal fairway"></div>
    <div class="body"><h3>Seacliff Links</h3><div class="date">November 16 , 2014</div><div class="joined">289 people joined</div><div class="progress"><span style="width:88%"></span></div><div class="quota">60 quota left</div></div>
  </article>
  <article class="abs event-card" style="left:610px;top:502px">
    <div class="thumb t3" role="img" aria-label="Photo of a clubhouse behind a golf green and pond"></div>
    <div class="body"><h3>Palmgrove Club</h3><div class="date">November 18 , 2014</div><div class="joined">21 people joined</div><div class="progress"><span style="width:26%"></span></div><div class="quota">49 quota left</div></div>
  </article>
  <article class="abs event-card" style="left:840px;top:502px">
    <div class="thumb t4" role="img" aria-label="Photo of a golf green with a flag and houses behind"></div>
    <div class="body"><h3>Vista Mar</h3><div class="date">November 19 , 2014</div><div class="joined">56 people joined</div><div class="progress"><span style="width:80%"></span></div><div class="quota">38 quota left</div></div>
  </article>
</section>

<section>
  <h2 class="abs big-title" style="top:944px;font-size:40px">Featured Auction Items</h2>
  <div class="abs tile" style="left:196px;top:1040px;width:348px;height:204px;background:linear-gradient(135deg,#3a2418,#6b4a2e 50%,#d9c8a8)" role="img" aria-label="Photo of a Japanese dish on a wooden table"><span class="label" style="bottom:4px">Japanese Cuisine</span></div>
  <div class="abs tile" style="left:554px;top:1040px;width:450px;height:360px;background:linear-gradient(160deg,#7a6a3c,#b59a5e 45%,#e8dcc2 75%,#caa978)" role="img" aria-label="Photo of a dinner table set with glasses and napkins"><span class="label" style="bottom:4px">Dinner with Marcus Hale</span></div>
  <div class="abs tile small" style="left:196px;top:1252px;width:140px;height:142px;background:linear-gradient(180deg,#7fa6d2,#9bb7d8 55%,#8a7b6a)" role="img" aria-label="Watercolour painting of a harbour town"><span class="label" style="bottom:6px">Water Painting<br>by Ellen Park</span></div>
  <div class="abs tile" style="left:346px;top:1252px;width:198px;height:380px;background:linear-gradient(180deg,#2f7fd0,#8fbfe8 35%,#c9d9e6 55%,#6e8f5c 75%,#b8b8a8)" role="img" aria-label="Photo of the Eiffel Tower seen from a long garden promenade"><span class="label" style="top:10px;left:8px">5 Days / 4 Nights<br>in Paris France</span></div>
  <div class="abs tile small" style="left:196px;top:1404px;width:140px;height:228px;background:linear-gradient(135deg,#e8d8b4,#8a6a3c 55%,#3a2a1a)" role="img" aria-label="Photo of a wine bottle and filled glass"><span class="label" style="top:4px">Case of Valle Rosa<br>Wine</span></div>
  <div class="abs tile" style="left:554px;top:1410px;width:450px;height:222px;background:linear-gradient(160deg,#f1c66a,#d7a04a 45%,#6a4a22)" role="img" aria-label="Photo of a mountain bicycle against a warm wall"><span class="label" style="bottom:4px">Ridgeline Bicycle</span></div>
</section>

<section>
  <h2 class="abs section-title" style="left:202px;top:1666px;color:var(--blue)">Categories</h2>
  <div class="cat-list">
    <a class="active" style="left:202px;top:1731px">Vestibulum ante</a>
    <a style="left:202px;top:1767px">Vestibulum ante</a>
    <a style="left:202px;top:1805px">Vestibulum ante</a>
    <a style="left:202px;top:1841px">Vestibulum ante</a>
    <a style="left:410px;top:1731px">Wine</a>
    <a style="left:410px;top:1767px">Travel</a>
    <a style="left:410px;top:1805px">Vestibulum ante</a>
    <a style="left:410px;top:1841px">Vestibulum ante</a>
    <a style="left:618px;top:1731px">Vestibulum ante</a>
    <a style="left:618px;top:1767px">Vestibulum ante</a>
    <a style="left:618px;top:1805px">Vestibulum ante</a>
    <a style="left:618px;top:1841px">Vestibulum ante</a>
    <a style="left:826px;top:1731px">Vestibulum ante</a>
    <a style="left:826px;top:1767px">Vestibulum ante</a>
    <a style="left:826px;top:1805px">Vestibulum ante</a>
    <a style="left:826px;top:1841px">Vestibulum ante</a>
  </div>
</section>

<section>
  <h2 class="abs big-title" style="top:1972px;font-size:34px;font-weight:400">Advanced Search</h2>
  <div class="abs field" style="left:166px;top:2082px;width:236px"><span class="key">Type</span><span class="val">Event<svg width="22" height="12" viewBox="0 0 22 12"><polyline points="2,2 11,10 20,2" fill="none" stroke="var(--green)" stroke-width="3"/></svg></span></div>
  <div class="abs field" style="left:456px;top:2082px;width:234px"><span class="key">Date</span><span class="val">November<svg width="22" height="12" viewBox="0 0 22 12"><polyline points="2,2 11,10 20,2" fill="none" stroke="var(--green)" stroke-width="3"/></svg></span></div>
  <div class="abs field" style="left:750px;top:2082px;width:306px"><span class="key">Location</span><span class="val">Please choose<svg width="22" height="12" viewBox="0 0 22 12"><polyline points="2,2 11,10 20,2" fill="none" stroke="var(--green)" stroke-width="3"/></svg></span></div>
  <div class="abs field" style="left:298px;top:2172px;width:446px"><span class="key" style="padding:0 14px">Keywords</span><span class="val">Type keywords here</span></div>
  <div class="abs btn-search" style="left:774px;top:2172px;width:126px;height:48px">Search</div>

  <article class="abs event-card" style="left:160px;top:2284px;width:206px;height:316px">
    <div class="thumb" role="img" aria-label="Photo of a parkland golf course with autumn trees"></div>
    <div class="body"><h3>Rivermoor Country Club</h3><div class="date">November 12 , 2014</div><div class="joined">56 people joined</div><div class="progress"><span style="width:82%"></span></div><div class="quota">38 quota left</div></div>
  </article>
  <article class="abs event-card" style="left:390px;top:2284px;width:206px;height:316px">
    <div class="thumb t2" role="img" aria-label="Photo of a golfer teeing off on a coastal fairway"></div>
    <div class="body"><h3>Seacliff Links</h3><div class="date">November 16 , 2014</div><div class="joined">289 people joined</div><div class="progress"><span style="width:88%"></span></div><div class="quota">60 quota left</div></div>
  </article>
  <article class="abs event-card" style="left:620px;top:2284px;width:206px;height:316px">
    <div class="thumb t3" role="img" aria-label="Photo of a clubhouse behind a golf green and pond"></div>
    <div class="body"><h3>Palmgrove Club</h3><div class="date">November 18 , 2014</div><div class="joined">21 people joined</div><div class="progress"><span style="width:26%"></span></div><div class="quota">49 quota left</div></div>
  </article>
  <article class="abs event-card" style="left:850px;top:2284px;width:206px;height:316px">
    <div class="thumb t4" role="img" aria-label="Photo of a golf green with a flag and houses behind"></div>
    <div class="body"><h3>Vista Mar</h3><div class="date">November 19 , 2014</div><div class="joined">56 people joined</div><div class="progress"><span style="width:80%"></span></div><div class="quota">38 quota left</div></div>
  </article>

  <div class="abs view-more" style="top:2638px">View more results</div>
  <svg class="abs" style="left:552px;top:2668px" width="96" height="40" viewBox="0 0 96 40"><polygon points="0,0 48,22 96,0 96,16 48,38 0,16" fill="#9a9a9a"/></svg>
</section>

<footer>
  <div class="abs footer-rule"></div>
  <div class="abs footer-rule2"></div>
  <div class="abs brand footer-brand"><span class="brand-dot"></span><span>GoodCaddie.com</span></div>
</footer>
</body>
</html>
```